I need an amazing business card!

I am the principle in my own software company that develops vexPad and mobile applications. I require a great business card design. I've attached my corporate logo (Thanks Tomasz!).
I would like the design to integrate the logo, my name, email address and skype account:
name Brent Halloway
email brenthalloway@zelqor.com
skype brenthalloway.net
I would like the back of the card to have a "write on me area" similar to the "write on me" card on this page, row 6:
http://us.pravik.com/design-templates/business-cards/#industry=Computing%20%26%20IT
As far as the rest - it's all you!
Updates
1) Please add an example telephone number as well.
Industry/Entity Type
Software
Look and feel
Each slider illustrates characteristics of the customer's brand and the style your logo design should communicate.

```html
<!DOCTYPE html>
<html lang="en">
<head>
<meta charset="utf-8">
<title>Zelqor – Business Card</title>
<link rel="stylesheet" href="https://fonts.googleapis.com/css2?family=Open+Sans:wght@400&display=swap">
<style>
  :root {
    --canvas: #e9e7e3;
    --card-dark: #595959;
    --card-light: #ffffff;
    --accent: #9dba3f;
    --brand-text: #ffffff;
    --name-text: #dcdcdc;
    --contact-text: #cfcfcf;
    --write-line: #9a9a9a;
  }
  * { margin: 0; padding: 0; box-sizing: border-box; }
  html, body {
    width: 1200px;
    height: 918px;
    overflow: hidden;
    background: var(--canvas);
    font-family: "Open Sans", sans-serif;
  }
  .sheet {
    width: 1200px;
    height: 918px;
    display: flex;
    align-items: center;
    justify-content: center;
    gap: 48px;
  }
  .card {
    position: relative;
    width: 540px;
    height: 308px;
    box-shadow: 0 6px 18px rgba(0, 0, 0, 0.18);
    overflow: hidden;
  }
  .card--front { background: var(--card-dark); }
  .card--back { background: var(--card-light); }

  .brand {
    position: absolute;
    left: 40px;
    top: 132px;
    display: flex;
    align-items: center;
    gap: 12px;
  }
  .brand__dot {
    width: 22px;
    height: 22px;
    background: var(--accent);
  }
  .brand__name {
    font-size: 28px;
    font-weight: 400;
    line-height: 1;
    color: var(--brand-text);
  }

  .holder {
    position: absolute;
    left: 258px;
    top: 100px;
    width: 270px;
  }
  .holder__name {
    font-size: 32px;
    font-weight: 400;
    line-height: 1.2;
    white-space: nowrap;
    color: var(--name-text);
    text-shadow: 0 1px 0 rgba(255,255,255,0.35), 0 -1px 1px rgba(0,0,0,0.45);
    margin-left: 16px;
  }
  .contact {
    list-style: none;
    margin-top: 22px;
    font-size: 14px;
    line-height: 1.6;
    white-space: nowrap;
    color: var(--contact-text);
  }

  .write-area {
    position: absolute;
    left: 120px;
    right: 90px;
    top: 78px;
    display: flex;
    flex-direction: column;
    gap: 62px;
  }
  .write-area__line {
    height: 1px;
    background: var(--write-line);
  }
</style>
</head>
<body>
  <main class="sheet">
    <section class="card card--front" aria-label="Card front">
      <div class="brand">
        <span class="brand__dot"></span>
        <span class="brand__name">zelqor</span>
      </div>
      <div class="holder">
        <h1 class="holder__name">Brent Halloway</h1>
        <ul class="contact">
          <li>Tel: 555 014 2273</li>
          <li>Email: brenthalloway@zelqor.com</li>
          <li>Skype: brenthalloway.net</li>
        </ul>
      </div>
    </section>

    <section class="card card--back" aria-label="Card back, write-on area">
      <div class="write-area">
        <div class="write-area__line"></div>
        <div class="write-area__line"></div>
        <div class="write-area__line"></div>
      </div>
    </section>
  </main>
</body>
</html>
```